Renowned Chiropractic Clinic needs unique and professional business card

We need a clean and professional looking business card that embodies our core values and stands for excellence. Highest standard of care and trustworthiness is what we want a future patient to connect to the design of the business card.
Ideally we want the design of the business card to be unique in nature and have a close connection to the SPINE as it is the core of what we do in our office - working with peoples spines.

Contact Information for Business Card

Font file is modified Nexa light and Montserrat medium. Colors are #5BC9E1, #666666, and #9dd5eb

On the front we would like to have the logo and the name of the office with an engaging, trustworthy and professional design.
On the back we need an area for our address, phone number and email address (This can be also be in the front).
On the back we would also like the slogan (this is however not a must and can also be on the front).

The HEXAGON (the design from the spine), could be an idea for the design to evolve around - this is however up to your professional creativity!

Requirements
Must have
• I want the design to primarily evolve around the HEXAGON shape and to have as few curves in it as possible. Therefore, making the design as "edgy" and "linear" as possible.

- Logo
- German Address Line (we are moving offices so we do not yet have a physical address so it would have to be a placeholder address for now that can be changed) --> Office Name (Line 1), Streetname (Line 2), Zip Code and Town (Line 3)
- email and phone number field
Nice to have
• Incorporation of the slogan "Kehren Sie Ihren Problemen den Rücken"

Please let your imagination run free :)!!! I am excited to work with you all to create an astonishing business card!

```html
<!DOCTYPE html>
<html lang="de">
<head>
<meta charset="utf-8">
<title>Chiropraxis Achsenpunkt – Visitenkarte</title>
<link rel="stylesheet" href="https://fonts.googleapis.com/css2?family=Montserrat:wght@300;400;500;600&display=swap">
<style>
  :root {
    --backdrop: #dcdcdc;
    --card: #58595b;
    --accent: #5bc9e1;
    --accent-soft: #9dd5eb;
    --ink-light: #e6e6e6;
    --ink-white: #ffffff;
  }
  html, body {
    margin: 0;
    width: 1200px;
    height: 1200px;
    overflow: hidden;
    background: var(--backdrop);
    font-family: "Montserrat", sans-serif;
  }
  .stage { position: relative; width: 1200px; height: 1200px; }
  .card { position: absolute; top: 329px; width: 448px; height: 514px; }
  .card--back { left: 118px; }
  .card--front { left: 638px; }
  .card-shape { fill: var(--card); }
  .card-frame { fill: none; stroke: var(--accent); stroke-width: 2.5; }
  .divider { stroke: var(--accent); stroke-width: 1.4; }
  .icon-badge { fill: var(--accent); }
  .icon-glyph { fill: var(--card); }
  .icon-stroke { fill: none; stroke: var(--card); stroke-width: 1.6; }
  .contact-text {
    fill: var(--ink-light);
    font-family: "Montserrat", sans-serif;
    font-weight: 300;
    font-size: 20.5px;
    text-anchor: middle;
  }
  .brand-name {
    fill: var(--accent);
    font-family: "Montserrat", sans-serif;
    font-weight: 400;
    font-size: 30px;
    text-anchor: middle;
  }
  .person-name {
    fill: var(--accent);
    font-family: "Montserrat", sans-serif;
    font-weight: 600;
    font-size: 29px;
    text-anchor: middle;
  }
  .person-role {
    fill: var(--ink-white);
    font-family: "Montserrat", sans-serif;
    font-weight: 400;
    font-size: 19px;
    text-anchor: middle;
  }
</style>
</head>
<body>
<main class="stage">

  <!-- Back side: contact details -->
  <svg class="card card--back" viewBox="0 0 448 514" aria-label="Kartenrückseite mit Kontaktdaten">
    <polygon class="card-shape" points="224,0 448,129 448,385 224,514 0,385 0,129"/>
    <polygon class="card-frame" points="224,17 433,138 433,376 224,497 15,376 15,138"/>

    <g class="contact-row">
      <line class="divider" x1="156" y1="91" x2="206" y2="91"/>
      <line class="divider" x1="242" y1="91" x2="292" y2="91"/>
      <polygon class="icon-badge" points="224,77 236,84 236,98 224,105 212,98 212,84"/>
      <path class="icon-glyph" d="M224 84.5a4.6 4.6 0 0 1 4.6 4.6c0 3.4-4.6 8.4-4.6 8.4s-4.6-5-4.6-8.4a4.6 4.6 0 0 1 4.6-4.6z"/>
      <circle cx="224" cy="89" r="1.7" fill="var(--accent)"/>
    </g>
    <text class="contact-text" x="224" y="130">1204 Birch Hollow Road</text>
    <text class="contact-text" x="224" y="156">Fairview, Alaska 99512</text>

    <g class="contact-row">
      <line class="divider" x1="156" y1="188" x2="206" y2="188"/>
      <line class="divider" x1="242" y1="188" x2="292" y2="188"/>
      <polygon class="icon-badge" points="224,174 236,181 236,195 224,202 212,195 212,181"/>
      <path class="icon-glyph" d="M219.5 182.5l2.4-.6 1.3 3-1.5 1.1a8 8 0 0 0 3.3 3.3l1.1-1.5 3 1.3-.6 2.4c-5.2.3-9.3-3.8-9-9z"/>
    </g>
    <text class="contact-text" x="224" y="230">907-555-0184</text>

    <g class="contact-row">
      <line class="divider" x1="156" y1="250" x2="206" y2="250"/>
      <line class="divider" x1="242" y1="250" x2="292" y2="250"/>
      <polygon class="icon-badge" points="224,236 236,243 236,257 224,264 212,257 212,243"/>
      <rect class="icon-stroke" x="220" y="243.5" width="8" height="13" rx="1.2"/>
    </g>
    <text class="contact-text" x="224" y="288">907-555-0139</text>

    <g class="contact-row">
      <line class="divider" x1="156" y1="310" x2="206" y2="310"/>
      <line class="divider" x1="242" y1="310" x2="292" y2="310"/>
      <polygon class="icon-badge" points="224,296 236,303 236,317 224,324 212,317 212,303"/>
      <rect class="icon-glyph" x="217.5" y="305.5" width="13" height="9"/>
      <path d="M217.5 305.5l6.5 5 6.5-5" fill="none" stroke="var(--accent)" stroke-width="1.2"/>
    </g>
    <text class="contact-text" x="224" y="346">info@achsenpunkt-praxis.com</text>

    <g class="contact-row">
      <line class="divider" x1="156" y1="369" x2="206" y2="369"/>
      <line class="divider" x1="242" y1="369" x2="292" y2="369"/>
      <polygon class="icon-badge" points="224,355 236,362 236,376 224,383 212,376 212,362"/>
      <circle class="icon-stroke" cx="224" cy="369" r="5.5"/>
      <line class="icon-stroke" x1="218.5" y1="369" x2="229.5" y2="369"/>
    </g>
    <text class="contact-text" x="224" y="404">achsenpunkt-praxis.com</text>
  </svg>

  <!-- Front side: practice name and person -->
  <svg class="card card--front" viewBox="0 0 448 514" aria-label="Kartenvorderseite mit Praxisname">
    <polygon class="card-shape" points="224,0 448,129 448,385 224,514 0,385 0,129"/>
    <polygon class="card-frame" points="224,17 433,138 433,376 224,497 15,376 15,138"/>

    <text class="brand-name">
      <tspan x="224" y="232">CHIROPRAXIS</tspan>
      <tspan x="224" y="270">ACHSENPUNKT</tspan>
    </text>

    <text class="person-name" x="224" y="339">MARTIN KELLER</text>
    <text class="person-role" x="224" y="365">Founder &amp; CEO</text>
  </svg>

</main>
</body>
</html>
```